Deal Email Template Design

I need a number of email templates designed for my deal website. The emails will be used to promote, market, and sell it's deals. Emails will be launched using an email marketing platform. I will work with chosen designer to detail the company description, branding, logos, etc.
Updates
Reason: I added details to project and would like to see some more bids. Please feel free to submit and ask any questions.
Thank you.
Target Market(s)
Casino Destination Travelers
Industry/Entity Type
It Company
Look and feel
Each slider illustrates characteristics of the customer's brand and the style your logo design should communicate.

```html
<!DOCTYPE html>
<html lang="en">
<head>
<meta charset="utf-8">
<title>BrightBet – Product Description</title>
<link rel="stylesheet" href="https://fonts.googleapis.com/css2?family=Source+Sans+3:wght@400;600&display=swap">
<style>
  :root {
    --brand-yellow: #fdd300;
    --ink: #1c1c1c;
    --ink-soft: #333333;
    --band-grey: #efefef;
    --rule-grey: #d6d6d6;
    --square-grey: #e2e2e2;
    --page: #ffffff;
  }
  * { box-sizing: border-box; margin: 0; padding: 0; }
  html, body { width: 847px; height: 1200px; overflow: hidden; background: var(--page); }
  body { font-family: "Source Sans 3", "Myriad Pro", Arial, sans-serif; color: var(--ink); position: relative; }

  .brand { position: absolute; display: flex; align-items: center; }
  .brand--header { left: 65px; top: 50px; gap: 18px; }
  .brand__mark { border-radius: 50%; background: var(--brand-yellow); flex: none; }
  .brand--header .brand__mark { width: 96px; height: 96px; }
  .brand__name { font-weight: 600; color: var(--ink); letter-spacing: -0.5px; }
  .brand--header .brand__name { font-size: 44px; }
  .brand--footer { left: 662px; top: 1147px; gap: 6px; }
  .brand--footer .brand__mark { width: 36px; height: 36px; }
  .brand--footer .brand__name { font-size: 19px; }

  .page-title { position: absolute; left: 61px; top: 222px; font-size: 43px; font-weight: 400; letter-spacing: -0.3px; }

  .spec-band { position: absolute; left: 62px; top: 310px; width: 736px; height: 29px; background: var(--band-grey); display: flex; align-items: center; }
  .spec-band__tab { width: 29px; height: 29px; background: var(--brand-yellow); }
  .spec-band__label { margin-left: 19px; font-size: 14.5px; color: var(--ink-soft); }

  .spec-table { position: absolute; left: 62px; top: 366px; width: 736px; border-collapse: collapse; font-size: 11px; color: var(--ink-soft); }
  .spec-table td { height: 33.5px; border-bottom: 1px solid var(--rule-grey); vertical-align: middle; }
  .spec-table tr:last-child td { border-bottom: none; }
  .spec-table .spec-item { width: 570px; border-right: 1px solid var(--rule-grey); }
  .spec-table .spec-step { text-align: right; }
  .spec-item svg { margin-right: 3px; vertical-align: -1px; }

  .intro { position: absolute; left: 62px; top: 526px; width: 740px; font-size: 17.4px; line-height: 27.5px; color: var(--ink); }

  .step { position: absolute; left: 0; width: 847px; }
  .step--one { top: 614px; }
  .step--two { top: 924px; height: 136px; overflow: hidden; }
  .step__number { position: absolute; left: 150px; top: 0; font-size: 23px; line-height: 30px; }
  .step__progress { position: absolute; left: 89px; top: 42px; display: flex; gap: 9px; }
  .step__progress span { width: 12px; height: 12px; background: var(--square-grey); }
  .step__progress span.is-done { background: var(--brand-yellow); }
  .step__body { position: absolute; left: 189px; top: 0; width: 580px; font-size: 12.4px; line-height: 19.3px; color: var(--ink-soft); }
  .step__body p + p { margin-top: 17px; }
</style>
</head>
<body>
  <header class="brand brand--header">
    <span class="brand__mark"></span>
    <span class="brand__name">BrightBet</span>
  </header>

  <h1 class="page-title">Product Description</h1>

  <div class="spec-band">
    <span class="spec-band__tab"></span>
    <span class="spec-band__label">Product Specifications</span>
  </div>

  <table class="spec-table">
    <tr><td class="spec-item"><svg width="7" height="8" viewBox="0 0 7 8"><path d="M0 0L7 4L0 8Z" fill="#fdd300"/></svg>Lorem ipsum dolor sit amet, consectetuer adipiscing elit</td><td class="spec-step">Step 1</td></tr>
    <tr><td class="spec-item"><svg width="7" height="8" viewBox="0 0 7 8"><path d="M0 0L7 4L0 8Z" fill="#fdd300"/></svg>Lorem ipsum dolor sit amet</td><td class="spec-step">Step 2</td></tr>
    <tr><td class="spec-item"><svg width="7" height="8" viewBox="0 0 7 8"><path d="M0 0L7 4L0 8Z" fill="#fdd300"/></svg>Lorem ipsum dolor sit amet, consectetuer</td><td class="spec-step">Step 3</td></tr>
    <tr><td class="spec-item"><svg width="7" height="8" viewBox="0 0 7 8"><path d="M0 0L7 4L0 8Z" fill="#fdd300"/></svg>Lorem ipsum dolor sit amet, consect</td><td class="spec-step">Step 4</td></tr>
  </table>

  <p class="intro">Lorem ipsum dolor sit amet, consectetuer adipiscing elit, sed diam nonummy nibh euismod tincidunt ut laoreet dolore magna aliquam erat volutpat.</p>

  <section class="step step--one">
    <span class="step__number">1</span>
    <div class="step__progress"><span class="is-done"></span><span></span><span></span><span></span></div>
    <div class="step__body">
      <p>Lorem ipsum dolor sit amet, consectetuer adipiscing elit, sed diam nonummy nibh euismod tincidunt ut laoreet dolore magna aliquam erat volutpat.</p>
      <p>Lorem ipsum dolor sit amet, consectetuer adipiscing elit, sed diam nonummy nibh euismod tincidunt ut laoreet dolore magna aliquam erat volutpat. Lorem ipsum dolor sit amet, consectetuer adipiscing elit, sed diam nonummy nibh euismod tincidunt ut laoreet dolore magna aliquam erat volutpat. Lorem ipsum dolor sit amet, consectetuer adipiscing elit, sed diam nonummy nibh euismod tincidunt ut laoreet dolore magna aliquam erat volutpat.</p>
      <p>Lorem ipsum dolor sit amet, consectetuer adipiscing elit, sed diam nonummy nibh euismod tincidunt ut laoreet dolore magna aliquam erat volutpat. Lorem ipsum dolor sit amet, consectetuer adipiscing elit, sed diam nonummy nibh euismod tincidunt ut laoreet dolore magna aliquam erat volutpat. Lorem ipsum dolor sit amet, consectetuer adipiscing elit, sed diam nonummy nibh euismod tincidunt ut laoreet dolore magna aliquam erat volutpat. Lorem ipsum dolor sit amet, consectetuer adipiscing elit, sed diam nonummy nibh euismod tincidunt ut laoreet dolore magna aliquam erat volutpat.</p>
    </div>
  </section>

  <section class="step step--two">
    <span class="step__number">2</span>
    <div class="step__progress"><span class="is-done"></span><span class="is-done"></span><span></span><span></span></div>
    <div class="step__body">
      <p>Lorem ipsum dolor sit amet, consectetuer adipiscing elit, sed diam nonummy nibh euismod tincidunt ut laoreet dolore magna aliquam erat volutpat.</p>
      <p>Lorem ipsum dolor sit amet, consectetuer adipiscing elit, sed diam nonummy nibh euismod tincidunt ut laoreet dolore magna aliquam erat volutpat. Lorem ipsum dolor sit amet, consectetuer adipiscing elit, sed diam nonummy nibh euismod tincidunt ut laoreet dolore magna aliquam erat volutpat. Lorem ipsum dolor sit amet, consectetuer adipiscing elit, sed diam nonummy nibh euismod tincidunt ut laoreet dolore magna aliquam erat volutpat.</p>
    </div>
  </section>

  <footer class="brand brand--footer">
    <span class="brand__mark"></span>
    <span class="brand__name">BrightBet</span>
  </footer>
</body>
</html>
```